A banner for a fully digital bank.

In need of banners for the “Q7 Bank”. Has to show us not as just another digital bank, but a bank in whom ordinary people can trust. We won’t charge overdraft fees, transaction fees etc as a normal stationary bank would. We also will work with crypto, and be as user friendly as possible.

Banking

```html
<!DOCTYPE html>
<html lang="en">
<head>
<meta charset="utf-8">
<title>Q7 Bank – Banners</title>
<link rel="stylesheet" href="https://fonts.googleapis.com/css2?family=Lexend:wght@400;500;600;700&display=swap">
<style>
  :root {
    --page: #ffffff;
    --brand-blue: #0b55b0;
    --teal: #0a84a8;
    --navy: #26203d;
    --gold: #b8890f;
    --green-top: #8fd43a;
    --green-bottom: #4f9e1a;
    --button-text: #1d3a0c;
    --white: #ffffff;
    --coin: #2f7fa8;
    --black: #000000;
  }
  * { margin: 0; padding: 0; box-sizing: border-box; }
  html, body { width: 1200px; height: 1000px; overflow: hidden; background: var(--page); }
  body { position: relative; font-family: "Lexend", sans-serif; }

  .banner { position: absolute; overflow: hidden; background: var(--white); }
  .banner-bg { position: absolute; inset: 0; width: 100%; height: 100%; }
  .banner-wide { left: 64px; top: 133px; width: 1088px; height: 137px; border-top: 1px solid #eee; }
  .banner-compact { left: 370px; top: 317px; width: 476px; height: 76px; border-top: 1px solid #e4e8d4; }

  .wordmark {
    position: absolute; display: flex; align-items: center;
    color: var(--brand-blue); font-weight: 600; white-space: nowrap;
  }
  .wordmark .mark { background: var(--brand-blue); display: block; }

  .banner-wide .wordmark { left: 26px; top: 48px; font-size: 30px; gap: 14px; }
  .banner-wide .mark { width: 34px; height: 34px; }
  .banner-compact .wordmark { left: 14px; top: 26px; font-size: 17px; gap: 8px; }
  .banner-compact .mark { width: 18px; height: 18px; }

  .tagline { position: absolute; color: var(--white); font-weight: 500; text-align: center; }
  .banner-wide .tagline { left: 370px; top: 20px; width: 490px; font-size: 30px; line-height: 52px; letter-spacing: 0.3px; }
  .banner-compact .tagline { left: 205px; top: 12px; width: 150px; font-size: 12.5px; line-height: 17px; }

  .cta {
    position: absolute; display: flex; align-items: center; justify-content: center;
    background: linear-gradient(var(--green-top), var(--green-bottom));
    color: var(--button-text); font-weight: 700; white-space: nowrap;
    border: 2px solid #a8e060;
  }
  .banner-wide .cta { left: 879px; top: 44px; width: 188px; height: 50px; border-radius: 12px; font-size: 20px; }
  .banner-compact .cta { left: 361px; top: 25px; width: 104px; height: 26px; border-radius: 7px; font-size: 11px; }

  .logo-panel {
    position: absolute; top: 600px; width: 600px; height: 400px;
    display: flex; align-items: center; justify-content: center;
  }
  .logo-panel.light { left: 0; background: var(--white); }
  .logo-panel.dark { left: 600px; background: var(--black); }
  .logo-panel .wordmark { position: static; font-size: 50px; gap: 24px; }
  .logo-panel .mark { width: 80px; height: 80px; }
</style>
</head>
<body>

<section class="banner banner-wide">
  <svg class="banner-bg" viewBox="0 0 1088 137" preserveAspectRatio="none">
    <defs>
      <linearGradient id="wideFill" x1="0" x2="1" y1="0" y2="0">
        <stop offset="0" stop-color="#0a8cb0"/>
        <stop offset="0.45" stop-color="#0e6f97"/>
        <stop offset="1" stop-color="#26203d"/>
      </linearGradient>
    </defs>
    <polygon points="256,0 1088,0 1088,137 356,137" fill="var(--gold)"/>
    <polygon points="272,0 1088,0 1088,137 372,137" fill="url(#wideFill)"/>
    <line x1="500" y1="0" x2="1088" y2="90" stroke="#12384f" stroke-width="4" opacity="0.5"/>
    <g role="img" aria-label="Faint coin and currency decoration">
      <circle cx="1050" cy="25" r="30" fill="var(--coin)" opacity="0.8"/>
      <ellipse cx="908" cy="112" rx="22" ry="14" fill="var(--coin)" opacity="0.6"/>
    </g>
  </svg>
  <div class="wordmark"><span class="mark"></span>Q7 BANK</div>
  <p class="tagline">Making Banking Smarter,<br>Safer and Simpler for you.</p>
  <a class="cta">SIGN UP NOW</a>
</section>

<section class="banner banner-compact">
  <svg class="banner-bg" viewBox="0 0 476 76" preserveAspectRatio="none">
    <defs>
      <linearGradient id="compactFill" x1="0" x2="1" y1="0" y2="0">
        <stop offset="0" stop-color="#0a8cb0"/>
        <stop offset="0.5" stop-color="#0e6f97"/>
        <stop offset="1" stop-color="#26203d"/>
      </linearGradient>
    </defs>
    <polygon points="140,0 476,0 476,76 204,76" fill="var(--gold)"/>
    <polygon points="148,0 476,0 476,76 214,76" fill="url(#compactFill)"/>
    <g role="img" aria-label="Faint coin and currency decoration">
      <circle cx="456" cy="14" r="14" fill="var(--coin)" opacity="0.8"/>
      <ellipse cx="378" cy="62" rx="12" ry="8" fill="var(--coin)" opacity="0.6"/>
    </g>
  </svg>
  <div class="wordmark"><span class="mark"></span>Q7 BANK</div>
  <p class="tagline">Making Banking Smarter, Safer and Simpler for you.</p>
  <a class="cta">SIGN UP NOW</a>
</section>

<div class="logo-panel light">
  <div class="wordmark"><span class="mark"></span>Q7 BANK</div>
</div>
<div class="logo-panel dark">
  <div class="wordmark"><span class="mark"></span>Q7 BANK</div>
</div>

</body>
</html>
```